web Design for Architecture and Interior Design Firm

This is a complete redesign of an architecture and interior design firm.( http://www.kelbrixa.com )
We have established a new look-n-feel for them and need to apply it to the new site/new architecture. Wireframes attached with logo and PDF of new brochure.
This will require a quck turn-around. The client is expecting a very modern design with web 2.0 in mind.
Again very quick turn-around! If you cannot commit to a Friday deliverable, do not bid! Must be completed by no later than Friday!

```html
<!DOCTYPE html>
<html lang="en">
<head>
<meta charset="utf-8">
<title>Varenne Holt Design Studios</title>
<link rel="stylesheet" href="https://fonts.googleapis.com/css2?family=Yanone+Kaffeesatz:wght@400;500&family=Arimo:wght@400;700&family=Open+Sans:wght@400;600&display=swap">
<style>
:root{
  --crimson:#821430;
  --crimson-deep:#5a0610;
  --red:#c8102e;
  --red-text:#9b0d1e;
  --slate:#6a6d78;
  --slate-light:#8d909a;
  --panel:#6b7690;
  --cream:#fcf8ee;
  --ink:#333333;
  --dark:#1d2a30;
  --white:#ffffff;
}
*{margin:0;padding:0;box-sizing:border-box}
html,body{width:1123px;height:1200px;overflow:hidden;background:var(--cream)}
body{position:relative;font-family:"Open Sans",Arial,sans-serif;color:var(--ink)}
.abs{position:absolute}

.masthead{left:0;top:0;width:1123px;height:214px;background:linear-gradient(180deg,#8a1834,#7a1029)}
.brand{left:45px;top:74px;display:flex;align-items:center;gap:14px}
.brand-mark{width:50px;height:50px;border:3px solid var(--crimson-deep)}
.brand-name{font-family:"Arimo",Arial,sans-serif;font-weight:700;font-size:30px;color:var(--crimson-deep);letter-spacing:1px;line-height:1;white-space:nowrap}
.badge{left:917px;top:34px;width:194px;height:81px;background:var(--white)}

.main-nav{left:43px;top:166px;width:1036px;height:48px;background:linear-gradient(180deg,#d2c8c8,#9c8e90);border-radius:12px 12px 0 0;display:flex;align-items:center;justify-content:center}
.main-nav ul{list-style:none;display:flex;flex-wrap:nowrap;align-items:center;font-family:"Arimo",Arial,sans-serif;font-weight:700;font-size:13.5px;line-height:1;color:var(--white)}
.main-nav li{white-space:nowrap;flex-shrink:0}
.main-nav li+li::before{content:"|";margin:0 11px;color:var(--white)}
.main-nav li.current{color:#1a1a1a}

.band{left:0;top:214px;width:1123px;height:45px;background:var(--crimson-deep)}
.hero{left:0;top:259px;width:1123px;height:417px;background:linear-gradient(180deg,var(--slate-light),var(--slate))}
.photo-frame{left:22px;top:233px;width:592px;height:433px;background:var(--white);box-shadow:0 3px 10px rgba(0,0,0,.4);transform:rotate(-.6deg)}
.photo{left:36px;top:261px;width:565px;height:379px;background:linear-gradient(160deg,#d9cfc0,#7a6650 60%,#3e3024)}

.welcome{left:636px;top:284px;width:475px;height:205px;background:var(--panel);border:1px solid #333;padding:14px 16px}
.welcome h1{font-family:"Yanone Kaffeesatz",sans-serif;font-weight:400;font-size:31px;color:#111;text-align:center;line-height:1.1;white-space:nowrap}
.welcome h1 span{color:var(--crimson-deep);font-size:46px;font-weight:500}
.welcome p{margin-top:10px;font-size:11.2px;line-height:1.4;color:var(--white)}
.btn-more{left:640px;top:498px;width:137px;height:34px;background:var(--red);border:1px solid #7a0a18;color:var(--white);font-size:12.5px;padding:8px 16px;white-space:nowrap}

.col-title{font-family:"Yanone Kaffeesatz",sans-serif;font-weight:500;font-size:26px;color:var(--red-text);padding-bottom:6px;border-bottom:1px dashed #555;white-space:nowrap}
.intro{left:26px;top:697px;width:630px}
.intro h3{margin-top:18px;font-size:12.5px;font-weight:600;color:var(--red-text)}
.intro p{font-size:11.5px;line-height:1.75}

.services{left:694px;top:697px;width:393px}
.service-box{left:697px;top:752px;width:391px;height:157px;background:var(--white);box-shadow:0 1px 5px rgba(0,0,0,.35);padding:12px}
.service-box ul{list-style:none;background:var(--red);height:100%;padding:14px 18px;color:var(--white);font-size:16px}
.service-box li{line-height:27px;white-space:nowrap}
.service-box li::before{content:"";display:inline-block;width:9px;height:9px;border:1px solid var(--white);margin-right:10px}

.values{left:26px;top:918px;width:630px}
.values ul{list-style:none;margin-top:16px;display:grid;grid-template-columns:318px 1fr;font-size:12.5px;font-weight:600;line-height:20px}
.values li{white-space:nowrap}
.values li::before{content:"▸";font-size:10px;margin-right:8px}

.contact{left:694px;top:918px;width:393px}
.contact dl{margin-top:10px;padding-left:8px;font-size:11.5px;line-height:20px}
.contact dt{display:inline;font-weight:700;color:var(--red-text)}
.contact dd{display:inline}
.contact address{margin-top:20px;padding-left:8px;font-style:normal;font-size:12.5px;font-weight:600;line-height:20px}

.footer{left:0;top:1131px;width:1123px;height:69px;background:var(--dark);color:var(--white);text-align:center;font-size:11.5px;padding-top:14px;line-height:22px;white-space:nowrap}
.footer nav span+span::before{content:"|";margin:0 10px}
</style>
</head>
<body>
<header class="abs masthead" aria-label="Masthead"></header>
<div class="abs brand"><span class="brand-mark"></span><span class="brand-name">VARENNE HOLT</span></div>
<div class="abs badge" role="img" aria-label="Anniversary badge"></div>

<nav class="abs main-nav">
  <ul>
    <li class="current">Home</li><li>About Us</li><li>Our Competitive Edge</li><li>Services</li><li>Portfolios</li><li>VHDS News</li><li>Career</li><li>Firm Events</li><li>Testimonials</li><li>Contact Us</li>
  </ul>
</nav>

<div class="abs band"></div>
<section class="abs hero" role="img" aria-label="Faded architectural floor plan background"></section>
<div class="abs photo-frame"></div>
<div class="abs photo" role="img" aria-label="Photo of a furnished living room with sofas and a wall-mounted TV"></div>

<div class="abs welcome">
  <h1>welcome to <span>VARENNE HOLT</span></h1>
  <p>Lorem ipsum dolor sit amet, consectetur adipiscing elit. Nulla odio velit, malesuada eget auctor vitae, consequat eget magna. Vivamus sit amet risus nisi, fringilla pulvinar enim. Maecenas euismod fringilla tortor sed lobortis. Aliquam euismod dapibus dui, sed interdum orci ultrices vel. Praesent luctus, sem nec egestas vestibulum, tortor orci laoreet mi, eget posuere nulla arcu quis neque. Sed est velit, imperdiet at tincidunt in, viverra id sem. Nulla pellentesque blandit dui. Vestibulum velit metus, semper et posuere nec, aliquam ut felis.</p>
</div>
<div class="abs btn-more">Read More</div>

<section class="abs intro">
  <h2 class="col-title">Faced with an Office Move, Expansion Or New Building?</h2>
  <h3>Varenne Holt Design Studios Makes the Process Predictable</h3>
  <p>When something as important as the very space in which your business lives and works is about to be disrupted, you should be confident you've chosen the right space and the best team to ensure a successful project. Rely on Varenne-Holt Design Studios to meet your needs and to make the process predictable. You can be assured that your project goals and objectives will be achieved.</p>
</section>

<section class="abs services"><h2 class="col-title">Our Services</h2></section>
<div class="abs service-box">
  <ul><li>Architectural</li><li>Engineering</li><li>Interior Design</li><li>Facility Management</li></ul>
</div>

<section class="abs values">
  <h2 class="col-title">Our Core Values:</h2>
  <ul>
    <li>Responsive service</li><li>Listening &amp; understanding your needs</li>
    <li>Friendly and fun to work with</li><li>Flexibility</li>
    <li>Client oriented focus</li><li>Creative problem solving</li>
    <li>Teamwork</li><li>Learning environment and knowledge sharing</li>
  </ul>
</section>

<section class="abs contact">
  <h2 class="col-title">Contact Us</h2>
  <dl>
    <dt>EMAIL:</dt> <dd>admin@kelbrixa.com</dd><br>
    <dt>PHONE:</dt> <dd>703.555.0142 x121</dd><br>
    <dt>FAX:</dt> <dd>703.555.0187</dd>
  </dl>
  <address>4417 Alder Crest Drive<br>Suite 220<br>Brookvale, VA 22090</address>
</section>

<footer class="abs footer">
  <nav><span>Home</span><span>About Us</span><span>Our Competitive Edge</span><span>Services</span><span>Portfolios</span><span>VHDS News</span><span>Career</span><span>Contact Us</span><span>Privacy Policy</span><span>Terms &amp; Conditions</span></nav>
  <div>© 2011 &nbsp;www.kelbrixa.com &nbsp;&nbsp;| &nbsp;&nbsp;All rights reserved</div>
</footer>
</body>
</html>
```